Car Advertisement Design. 2090mm (H) x 4730mm(W)

Need a car exterior design for the kitchen company. Size is 2090mm (H) x 4730mm(W)

Target Market(s)

30-50 years

Requirements
Must have
• company logo and pics

```html
<!DOCTYPE html>
<html lang="en">
<head>
<meta charset="utf-8">
<title>BrightNook Interiors – Vehicle Wrap Panel</title>
<link rel="stylesheet" href="https://fonts.googleapis.com/css2?family=Montserrat:wght@400;600&display=swap">
<style>
  :root {
    --page-bg: #e1e6ec;
    --panel-bg: #ffffff;
    --brand-blue: #2a5ea8;
    --blue-light: #1f8fd6;
    --blue-deep: #1b3f9a;
    --brand-green: #6cbe45;
    --text-light: #ffffff;
  }
  html, body {
    margin: 0;
    padding: 0;
    width: 1200px;
    height: 1053px;
    overflow: hidden;
    background: var(--page-bg);
    font-family: "Montserrat", Arial, sans-serif;
  }
  .wrap-panel {
    position: absolute;
    left: 20px;
    top: 270px;
    width: 1160px;
    height: 512px;
    background: var(--panel-bg);
    overflow: hidden;
  }
  .wrap-art {
    position: absolute;
    inset: 0;
    width: 100%;
    height: 100%;
    display: block;
  }
  .brand {
    position: absolute;
    left: 0;
    width: 444px;
    top: 16px;
    text-align: center;
  }
  .brand-mark {
    display: block;
    width: 70px;
    height: 70px;
    margin: 0 auto 10px;
    background: var(--brand-green);
  }
  .brand-name {
    font-size: 27px;
    font-weight: 600;
    color: var(--brand-blue);
    letter-spacing: -0.5px;
  }
  .contact {
    position: absolute;
    left: 0;
    width: 444px;
    top: 252px;
    text-align: center;
    color: var(--text-light);
  }
  .contact-phone {
    font-size: 36px;
    font-weight: 600;
    margin: 0;
    line-height: 1.1;
  }
  .contact-web {
    font-size: 23px;
    font-weight: 400;
    margin: 8px 0 6px;
  }
  .contact-address {
    font-size: 17px;
    font-weight: 400;
    line-height: 1.35;
    margin: 0;
  }
</style>
</head>
<body>
  <main class="wrap-panel">
    <svg class="wrap-art" viewBox="0 0 1232 543" preserveAspectRatio="none" aria-hidden="false">
      <defs>
        <linearGradient id="blueFill" x1="0" y1="0" x2="1" y2="0">
          <stop offset="0" stop-color="var(--blue-light)"/>
          <stop offset="1" stop-color="var(--blue-deep)"/>
        </linearGradient>
        <linearGradient id="kitchenTones" x1="0" y1="0" x2="1" y2="1">
          <stop offset="0" stop-color="#eceeef"/>
          <stop offset="0.35" stop-color="#c99a72"/>
          <stop offset="0.6" stop-color="#e4e6e8"/>
          <stop offset="1" stop-color="#a86d43"/>
        </linearGradient>
      </defs>

      <path class="kitchen-photo" role="img" aria-label="Photo of a modern kitchen with walnut cabinets, white counters and stainless appliances"
            fill="url(#kitchenTones)"
            d="M470,170 C520,150 560,135 600,122 C800,62 1000,52 1232,92 L1232,543 L470,543 Z"/>

      <path class="contact-field" fill="url(#blueFill)"
            d="M0,152 C200,212 380,200 470,170 L470,462 C350,430 150,420 0,470 Z"/>

      <path class="accent-wave" fill="var(--brand-green)"
            d="M0,98 C200,180 380,168 600,88 C800,20 1000,14 1232,58 L1232,94 C1000,52 800,62 600,124 C390,196 200,214 0,154 Z"/>

      <path class="accent-sliver" fill="var(--brand-green)"
            d="M0,500 C90,522 180,514 250,496 C180,530 80,540 0,534 Z"/>
    </svg>

    <header class="brand">
      <span class="brand-mark"></span>
      <div class="brand-name">BrightNook Interiors</div>
    </header>

    <section class="contact">
      <p class="contact-phone">403.555.0142</p>
      <p class="contact-web">www.brightnookinteriors.ca</p>
      <p class="contact-address">218 Maple Avenue NE Calgary,<br>Alberta, T2A 0B5</p>
    </section>
  </main>
</body>
</html>
```